Design four banner ads for our upcoming revamped website

We need four banner ads for our website.

The link of our website is http://beta.mervatrade.com/

The banners will appear under the "Promotions" tab which is currently exhibiting placeholder images.

The titles for each of the banner ads are as follow:
1) Double Credit Chance
2) Capital Protection Scheme
3) Trade Bonus
4) 2.5% Annual Interest

Target Market(s)

forex traders

Requirements
Must have
• The banners must adhere and blend with the website existing theme
Should not have
• Please do not use any human figures in the banner or pictures of humans waving around cash.

```html
<!DOCTYPE html>
<html lang="en">
<head>
<meta charset="utf-8">
<title>Mervatrade – Promotions</title>
<link rel="stylesheet" href="https://fonts.googleapis.com/css2?family=Catamaran:wght@500;600;700&family=Roboto+Condensed:wght@300&display=swap">
<style>
  :root {
    --brand-orange: #f5821f;
    --wordmark-ink: #333333;
    --white: #ffffff;
    --tab-blue: #3a87c8;
    --tab-ink: #333333;
    --btn-blue: #4a9fd5;
    --btn-green: #3cb043;
    --btn-red: #ff0000;
    --banner-light: #d8d8d8;
    --banner-dark: #7c7c7c;
    --dot-grey: #cccccc;
    --ink: #111111;
  }
  * { box-sizing: border-box; margin: 0; padding: 0; }
  html, body { width: 1200px; height: 627px; overflow: hidden; background: var(--white); }
  body { position: relative; font-family: "Catamaran", sans-serif; }

  .hero-band {
    position: absolute; left: 0; top: 0; width: 1200px; height: 207px;
    background: var(--brand-orange);
  }
  .site-header {
    position: absolute; left: 0; top: 0; width: 1192px; height: 81px;
    background: var(--white);
    border-radius: 0 0 6px 6px;
    box-shadow: 0 1px 3px rgba(0,0,0,.15);
  }
  .brand {
    position: absolute; left: 151px; top: 22px;
    font-weight: 600; font-size: 30px; line-height: 1; color: var(--wordmark-ink);
  }

  .header-actions { position: absolute; top: 34px; left: 788px; display: flex; gap: 5px; }
  .btn {
    height: 25px; display: flex; align-items: center; gap: 3px;
    padding: 0 3px; border-radius: 3px; white-space: nowrap;
    color: var(--white); font-weight: 600; font-size: 11px; line-height: 1;
  }
  .btn svg { width: 14px; height: 14px; flex: none; }
  .btn-register { width: 108px; background: var(--btn-blue); }
  .btn-login { width: 52px; background: var(--btn-green); }
  .btn-language { width: 90px; background: var(--btn-red); font-size: 10px; position: relative; padding-left: 4px; }
  .lang-flag { width: 15px; height: 10px; background: #1f3a78; border: 1px solid var(--white); flex: none; }
  .lang-caret { position: absolute; right: 6px; top: 9px; width: 8px; height: 8px; }

  .value-points { position: absolute; top: 81px; left: 130px; display: flex; }
  .value-point {
    width: 186px; text-align: center;
    color: var(--white); font-weight: 600; font-size: 12px; line-height: 17.6px;
    padding: 0 4px;
  }

  .tabs { position: absolute; top: 173px; left: 453px; display: flex; height: 34px; }
  .tab { display: flex; align-items: center; font-size: 14px; font-weight: 500; }
  .tab-active { width: 99px; justify-content: center; background: var(--white); color: var(--tab-blue); }
  .tab-idle { width: 99px; color: var(--tab-ink); padding-left: 13px; }

  .promo-banner {
    position: absolute; left: 221px; top: 241px; width: 731px; height: 329px;
    background: linear-gradient(90deg, var(--banner-dark) 0%, var(--banner-light) 35%, var(--banner-light) 65%, var(--banner-dark) 100%);
    border-bottom: 3px solid #e4e4e4;
  }
  .promo-title {
    position: absolute; top: 44px; left: 0; width: 100%; text-align: center;
    font-family: "Roboto Condensed", sans-serif; font-weight: 300;
    font-size: 34px; letter-spacing: 4px; color: var(--ink); line-height: 1;
  }
  .promo-icon {
    position: absolute; left: 301px; top: 111px; width: 133px; height: 150px;
    border-radius: 8px;
    background: radial-gradient(circle at 50% 55%, #f5821f 0%, #f5a05a 55%, rgba(245,130,31,0.2) 100%);
  }
  .promo-shadow {
    position: absolute; left: 341px; top: 281px; width: 57px; height: 5px;
    border-radius: 50%; background: rgba(60,60,60,.55); filter: blur(1.5px);
  }

  .carousel-dots { position: absolute; top: 585px; left: 559px; display: flex; gap: 6px; }
  .carousel-dot { width: 12px; height: 12px; background: var(--dot-grey); }
  .carousel-dot.is-current { background: var(--brand-orange); }
</style>
</head>
<body>
  <div class="hero-band"></div>

  <header class="site-header">
    <div class="brand">Mervatrade</div>
    <nav class="header-actions">
      <div class="btn btn-register">
        <svg viewBox="0 0 16 16"><rect x="1.5" y="3" width="11" height="11" fill="none" stroke="#fff" stroke-width="1.6"/><path d="M6 10 L14 2" stroke="#fff" stroke-width="2.2"/></svg>
        Register Account
      </div>
      <div class="btn btn-login">
        <svg viewBox="0 0 16 16"><path d="M9 2h5v12H9" fill="none" stroke="#fff" stroke-width="1.6"/><path d="M2 8h8M7 5l3 3-3 3" fill="none" stroke="#fff" stroke-width="1.8"/></svg>
        Login
      </div>
      <div class="btn btn-language">
        <span class="lang-flag"></span>
        English
        <svg class="lang-caret" viewBox="0 0 8 8"><path d="M1 2.5l3 3 3-3" fill="none" stroke="#7a0000" stroke-width="1.2"/></svg>
      </div>
    </nav>
  </header>

  <section class="value-points">
    <p class="value-point">An expanding brand that enjoys recognition and trust for their resolute commitments</p>
    <p class="value-point">Achieve your maximum potential by taking advantage of our diversified products</p>
    <p class="value-point">Establish a sustainable relationship geared towards growth and global expansion</p>
    <p class="value-point">Maximize your profits by leveraging on benefits designed just for you</p>
    <p class="value-point">Protect your funds from volatile markets by having instant access to crucial information</p>
  </section>

  <div class="tabs">
    <div class="tab tab-active">Promotions</div>
    <div class="tab tab-idle">Contents</div>
  </div>

  <section class="promo-banner">
    <h2 class="promo-title">TRADE BONUS</h2>
    <div class="promo-icon" role="img" aria-label="Orange outline gift box with a ribbon bow"></div>
    <div class="promo-shadow"></div>
  </section>

  <div class="carousel-dots">
    <span class="carousel-dot is-current"></span>
    <span class="carousel-dot"></span>
    <span class="carousel-dot"></span>
    <span class="carousel-dot"></span>
  </div>
</body>
</html>
```